Interactive Children's Media Book Company Website Design

We need a website DESIGN (no coding required) for a new interactive children's media book company called Tovira Studios.

We develop high-quality interactive children's books for the Slate/Pocketphone that seeks to delight and inspire young and old alike. Our stories are filled with heart and spirit, and we seek to breathe magic back into books so that people fall back in love with reading.

Tovira means "butterfly" in Korean. It plays on the idea that a caterpillar metamorphoses into a butterfly - and in the same way, our readers are transformed through the journey of experiencing our interactive books.

We're looking for something based on the ATTACHED LOGO DESIGN for our company. A website that's professional, modern, fun and inviting; easy to read and not-cluttered, but still portraying the feeling of innocence and childhood.

We're looking for something that resonates the magical experience we want to create for our readers. Specific requirements on pages, tabs, content, etc are below.

Industry/Entity Type

It Company

Requirements
Nice to have
• There are 7 tabs on the Homepage of the website: HOME, GRANDPA, ABOUT US, CAREERS, NEWS, CONTACT US, SHOP. (But there is an extra page called THEIR GARDEN, which will be a sub-page under Grandpa).

HOME
• Would be great to have some key images of our book (3-4 screen shots) as the key focus of the homepage that automatically scroll through every few seconds. (Placeholder image attached). The images would link to the “Grandpa” page.
• Company logo (attached to brief) and slogan: “A new era of children’s media” quite prominent on page.
• Key text content to be on page: “Tovira means “butterfly” in Korean. Just as a caterpillar transforms into a butterfly, Tovira Studios takes the reader on an unforgettable journey of metamorphosis through our stories. We turn children’s books into a high-quality interactive experience on mobile platforms - breathing magic back into books, and inspiring people to fall back in love with reading. Through our unique characters full of heart and spirit, our stories delight and inspire young and old alike.”
• Chirper & Friendbook Like & Friendbook page link icons.
• Section on Latest News with a few of the latest entries.
• Section on latest sister images & comments that visitors have posted, which takes you to the “Their Garden” page.

GRANDPA
• The title for this page is “Grandpa Keeps a Secret Garden”
• There will be a little Slate/Pocketphone icon (placeholder attached) for this book.
• There will be a link to the App Market to buy the app book.
• Key text content on this page: “Our debut interactive media book is coming soon on the Slate and Pocketphone! “Grandpa Keeps a Secret Garden” touches on the beautiful and inextricable (albeit sometimes frustrating!) bond between sisters.”
• There will be a section on “Features” which lists all the various special features the app book includes.
• There will be a YouTube clip embedded into the page, which shows how the app book works.
• A section that says: “Do you have a sister who’s not like other sisters? Share a photo and tell us about her!” which links to the sub-page “Their Garden”.
• Under this, there may be the most recent few images submitted by the public, which when clicked on, would also link to the sub-page “Their Garden”.

THEIR GARDEN
• The main text on the page: “Do you have a sister who’s not like other sisters? Share a photo and tell us about her!”
• Main body of the page is a gallery of all the photos that have been submitted. If you click on each of the images, you get the comments that people have submitted with the photos.
• The page would also have a Submit Comments Form, where people can upload a picture of their sister(s) and write a comment to accompany the image.

ABOUT US
• Introductory text on page: “It was a chance conversation at Harbourview Terminal, where two friends discovered they shared a dream to create quality children's media. Both of them were excited by the possibilities of using new digital platforms to inspire and educate a younger generation. From that idea Tovira Studios was born. We seek to be the chrysalis of story telling - to inspire the hearts and minds of our generation, and generations to come.”
• Section to “Join the Mailing List” where they can put their email address in and submit.
• Bios of 2x people with photos (bios in word doc attached) (do not have photos yet).

CAREERS
• The main text on the page: “We are always on the lookout for talented people to join our team. If you are a writer, illustrator, animator, iOS/android developer, musician, creative-writing translator - or have something special to offer Tovira Studios - we are keen to hear from you. Send us a message through the Contact Us tab above.”

NEWS
• Regular News page, with blog-type entries.

CONTACT US
• Online submit Contact Us form
• The main text on page: “Our studio is based in the Marram Arts Hub, 14 Pellham Street, Ardlow, Wellington. Marram is a professional, creative collective - with four separate studios, gallery, and retail store. For more information on Marram, visit: http://www.marramhub.example.nz”
• “We would love to hear from you! Whether you have questions, ideas, comments, or just want to say hullo - please leave us a message and we will get back to you soon.”
• Including image of the premises (Marram image attached to brief).

SHOP
• Where visitors can purchase merchandise (t-shirts, mugs, etc) of the book/company.

```html
<!DOCTYPE html>
<html lang="en">
<head>
<meta charset="utf-8">
<title>Grandpa Page – Tovira Studios</title>
<link rel="stylesheet" href="https://fonts.googleapis.com/css2?family=Arimo:ital,wght@0,400;0,700;1,400&family=Kalam&display=swap">
<style>
:root{
  --ink:#111;
  --navy:#20406e;
  --sky:#9dd6f6;
  --sky-deep:#6cc3f0;
  --sky-soft:#c9e9fb;
  --grey-panel:#efefef;
  --tab-top:#bdbdbd;
  --tab-bottom:#7e7e7e;
  --frame:#222;
  --white:#fff;
  --brand:#7a6fd8;
  --gold:#e5c64a;
}
*{box-sizing:border-box;margin:0;padding:0}
html,body{width:1200px;height:900px;overflow:hidden;background:var(--white)}
body{position:relative;font-family:"Arimo",Arial,sans-serif;color:var(--ink)}
.page{position:absolute;left:66px;top:100px;width:1070px;height:636px;border:2px solid var(--frame);background:var(--white);overflow:hidden}
.abs{position:absolute}

/* header */
.topline{left:290px;top:0;right:0;height:8px;background:#000}
.brand{left:20px;top:14px;width:260px;height:90px;display:flex;align-items:center;gap:14px}
.brand-dot{width:42px;height:42px;border-radius:50%;background:var(--brand)}
.brand-name{font-size:40px;font-weight:400;color:var(--brand);letter-spacing:1px}
.nav{left:290px;top:12px;right:0;height:36px;display:flex}
.nav a{flex:1;display:flex;align-items:flex-start;justify-content:center;padding-top:5px;font-size:13px;font-weight:700;color:var(--white);text-decoration:none;background:linear-gradient(var(--tab-top),var(--tab-bottom));border-right:1px solid #ddd}
.nav a.is-active{background:var(--sky-deep)}
.subnav{left:478px;top:48px;width:108px;height:38px;background:var(--sky);border:1px solid #7fb9dc;display:flex;align-items:center;justify-content:center;font-size:13px;font-weight:700;color:var(--white)}

/* features column */
.features-head{left:0;top:138px;width:292px;height:110px;background:var(--sky);text-align:center;padding-top:16px;color:var(--navy)}
.features-head h2{font-size:22px;font-weight:700;letter-spacing:.5px}
.features-head p{font-size:14px;font-weight:700;line-height:20px;margin-top:6px}
.features-body{left:0;top:248px;width:292px;height:388px;background:var(--grey-panel)}
.lorem{font-size:10px;line-height:24px}
.features-body .lorem{position:absolute;left:68px;top:16px}
.instructions{left:70px;top:176px;font-size:15px;font-weight:700;display:flex;align-items:center;gap:6px;white-space:nowrap}
.instructions span{width:12px;height:10px;background:#d9534f;display:inline-block}
.video{left:68px;top:214px;width:202px;height:130px;border:1px solid #666;background:#e6e6e6}

/* book column */
.book{left:294px;top:138px;width:430px;height:498px;background:var(--sky-soft)}
.book-card{left:8px;top:0;width:414px;height:398px;background:var(--white)}
.soon{left:18px;top:6px;width:380px;height:50px;background:var(--sky);display:flex;align-items:center;gap:10px;padding-left:6px}
.soon-icon{flex:none}
.soon p{font-size:15px;font-weight:700;color:var(--navy);line-height:19px;text-align:center}
.book-title{left:0;top:84px;width:414px;text-align:center;font-size:20px;font-weight:700;letter-spacing:.4px;white-space:nowrap}
.cover{left:72px;top:124px;width:104px;height:138px;border:2px solid #333;background:linear-gradient(#7fd0d8,#e98a3c)}
.store-badge{left:244px;top:170px;width:160px;height:34px;border-radius:6px;background:#5a5a5a}
.order{left:244px;top:224px;width:160px;text-align:center;font-size:14px;font-weight:700}
.blurb{left:22px;top:272px;width:370px;font-family:"Kalam",cursive;font-style:italic;font-size:17px;line-height:23px;color:#333}
.social{left:0;top:398px;width:430px;height:100px;background:var(--sky-deep);display:flex;color:var(--white)}
.social-item{flex:1;padding-top:12px;display:flex;flex-direction:column;align-items:center}
.social-item h3{font-size:11px;font-weight:700;letter-spacing:.3px;white-space:nowrap}
.social-link{display:flex;align-items:center;gap:10px;margin-top:18px}
.social-link i{width:30px;height:30px;background:var(--navy);display:block}
.social-link b{font-size:16px;font-weight:700;color:var(--white)}

/* share column */
.share-head{left:728px;top:138px;width:342px;height:100px;background:var(--sky);padding:12px 20px 0 58px;font-size:15px;font-weight:700;line-height:20px;color:var(--navy)}
.share-tab{left:728px;top:248px;width:116px;height:30px;background:var(--sky);display:flex;align-items:center;justify-content:center;font-size:12px;font-weight:700;color:var(--white)}
.share-body{left:728px;top:278px;width:342px;height:358px;border-left:2px solid #ddd}
.photo{width:116px;height:116px;border:2px solid #444;background:#d3d3d3;display:flex;align-items:center;justify-content:center;font-size:11px;color:var(--white)}
.photo-a{left:42px;top:20px}
.photo-b{left:200px;top:20px}
.share-body .lorem{position:absolute;left:40px;top:180px;line-height:22px}

.caption{left:0;top:784px;width:1200px;text-align:center;font-size:16px}
</style>
</head>
<body>
<main class="page">
  <div class="abs topline"></div>
  <div class="abs brand"><span class="brand-dot"></span><span class="brand-name">tovira</span></div>
  <nav class="abs nav">
    <a href="#">Home</a><a href="#" class="is-active">Grandpa</a><a href="#">About Us</a><a href="#">Careers</a><a href="#">News</a><a href="#">Contact Us</a><a href="#">Shop</a>
  </nav>
  <div class="abs subnav">Their Garden</div>

  <section class="abs features-head">
    <h2>FEATURES</h2>
    <p>Grandpa Keeps a Secret Garden<br>App Includes the Following:</p>
  </section>
  <section class="abs features-body">
    <p class="lorem">Lorem ipsum dolor sit amet,<br>consectetur adipiscing elit.<br>Suspendisse vehicula pretium<br>sapien, non pellentesque nisl<br>semper nec. Aenean ornare,<br>augue eu egestas tincidunt,</p>
    <div class="abs instructions">App Instructions <span></span></div>
    <svg class="abs video" viewBox="0 0 202 130" role="img" aria-label="Embedded video showing how the app book works">
      <rect width="202" height="130" fill="#e6e6e6"/>
      <rect x="0" y="112" width="202" height="18" fill="#cfcfcf"/>
      <rect x="84" y="44" width="34" height="34" fill="var(--gold)"/>
      <path d="M95 52 L110 61 L95 70 Z" fill="#888"/>
    </svg>
  </section>

  <section class="abs book">
    <div class="abs book-card">
      <div class="abs soon">
        <svg class="soon-icon" width="30" height="30" viewBox="0 0 30 30" aria-hidden="true"><circle cx="15" cy="15" r="9" fill="var(--gold)"/></svg>
        <p>Our Deput Interactive Media Book is<br>COMING SOON on Slate and Pocketphone</p>
      </div>
      <h1 class="abs book-title">GRANDPA KEEPS A SECRET GARDEN</h1>
      <div class="abs cover" role="img" aria-label="Book character artwork"></div>
      <div class="abs store-badge" role="img" aria-label="App market badge"></div>
      <div class="abs order">ORDER NOW</div>
      <p class="abs blurb">Grandpa Keeps a Secret Garden touches on the beautiful and inextricable (albeit sometimes frustrating) bond between sisters</p>
    </div>
    <div class="abs social">
      <div class="social-item"><h3>LIKE OUR FRIENDBOOK PAGE</h3><div class="social-link"><i></i><b>Friendbook</b></div></div>
      <div class="social-item"><h3>FOLLOW US ON CHIRPER</h3><div class="social-link"><i></i><b>Chirper</b></div></div>
    </div>
  </section>

  <section class="abs share-head">Do you have a grandpa with a garden all his own? Share a photo and tell us about him...</section>
  <div class="abs share-tab">Their Garden</div>
  <section class="abs share-body">
    <div class="abs photo photo-a">Picture</div>
    <div class="abs photo photo-b">Picture</div>
    <p class="lorem">Lorem ipsum dolor sit amet,<br>consectetur adipiscing elit.<br>Suspendisse vehicula pretium<br>sapien, non pellentesque nisl<br>semper nec. Aenean ornare,<br>augue eu egestas tincidunt,</p>
  </section>
</main>
<p class="abs caption">Grandpa Page</p>
</body>
</html>
```